Young, dynamic furniture company needs a new business card design

We require a new business card design for our modern furniture company which supplies furniture and appliances to the property and development market.
Oakline Furnishings has become one of the leading furniture & appliance suppliers to the property market withing London. With over 10 years experience, we have increased our business to supply not only private landlords and managing agents, but also property developers, housing associations and local councils.
We offer not only a complete range of furniture which includes beds, wardrobes, dining sets and sofas, but also a high quality, full delivery and assembly service to help you with all our furnishing needs.

Target Market(s)

Private landlords, estate agents, letting agents, property management companies

Industry/Entity Type

Business

Contact Information for Business Card

Name,
Title,
Address,
Mobile,
Telephone,
Fax, Website, email address

Font styles to use
Sans Serif

Colors
3176b5
0555a3
85abd2
cfdeed

Requirements
Must have
• All the above information for each of our staff, along with our logo

```html
<!DOCTYPE html>
<html lang="en">
<head>
<meta charset="utf-8">
<title>Oakline Furnishings – Business Card</title>
<link href="https://fonts.googleapis.com/css2?family=Montserrat:wght@400;500;700&family=Roboto+Condensed:wght@300;400&display=swap" rel="stylesheet">
<style>
  :root {
    --stage: #131313;
    --navy: #1f3a6e;
    --brand-blue: #1e6fb8;
    --ink: #1a1a1a;
    --white: #ffffff;
  }
  html, body {
    margin: 0;
    padding: 0;
    width: 1189px;
    height: 1200px;
    overflow: hidden;
    background: var(--stage);
  }
  .canvas {
    position: relative;
    width: 1189px;
    height: 1200px;
  }
  .card {
    position: absolute;
    top: 145px;
    width: 483px;
    height: 846px;
    border-radius: 23px;
    overflow: hidden;
  }

  /* Back side */
  .card--back {
    left: 73px;
    background: var(--navy);
  }
  .vertical {
    position: absolute;
    writing-mode: vertical-rl;
    transform: rotate(180deg);
    font-family: "Roboto Condensed", sans-serif;
    color: var(--white);
    white-space: nowrap;
    margin: 0;
  }
  .vertical--name {
    left: 178px;
    bottom: 105px;
    font-weight: 300;
    font-size: 76px;
    line-height: 1;
  }
  .vertical--tagline {
    left: 262px;
    bottom: 138px;
    font-weight: 300;
    font-size: 35px;
    line-height: 1;
  }

  /* Front side */
  .card--front {
    left: 630px;
    background: var(--white);
  }
  .brand {
    position: absolute;
    top: 70px;
    left: 0;
    width: 100%;
    text-align: center;
  }
  .brand__mark {
    width: 170px;
    height: 170px;
    margin: 0 auto 52px;
    background: var(--navy);
  }
  .brand__name {
    margin: 0;
    font-family: "Roboto Condensed", sans-serif;
    font-weight: 400;
    font-size: 40px;
    line-height: 40px;
    color: var(--ink);
  }
  .brand__tagline {
    margin: 0;
    font-family: "Roboto Condensed", sans-serif;
    font-weight: 400;
    font-size: 21px;
    line-height: 23px;
    color: var(--ink);
  }
  .details {
    position: absolute;
    left: 56px;
    top: 412px;
    font-family: "Montserrat", sans-serif;
    color: var(--ink);
  }
  .person__name {
    margin: 0;
    font-weight: 700;
    font-size: 31px;
    line-height: 31px;
    color: var(--navy);
  }
  .person__surname { color: var(--brand-blue); }
  .person__role {
    margin: 3px 0 0;
    font-size: 23px;
    line-height: 26px;
  }
  .address {
    margin: 30px 0 0;
    font-style: normal;
    font-size: 23px;
    line-height: 29px;
  }
  .contacts {
    list-style: none;
    margin: 21px 0 0;
    padding: 0;
    font-size: 23px;
    line-height: 32px;
  }
  .contacts__label {
    display: inline-block;
    width: 34px;
    padding-left: 4px;
    color: var(--navy);
    font-weight: 500;
  }
  .footer-rule {
    position: absolute;
    left: 0;
    top: 775px;
    width: 100%;
    height: 4px;
    background: var(--brand-blue);
  }
  .footer-band {
    position: absolute;
    left: 0;
    top: 783px;
    width: 100%;
    height: 63px;
    background: var(--navy);
    color: var(--white);
    font-family: "Montserrat", sans-serif;
    font-weight: 500;
    font-size: 23px;
    line-height: 63px;
    text-align: center;
  }
</style>
</head>
<body>
<main class="canvas">
  <section class="card card--back" aria-label="Card back">
    <h1 class="vertical vertical--name">OAKLINE FURNISHINGS</h1>
    <p class="vertical vertical--tagline">TRADE FURNITURE SOLUTIONS</p>
  </section>

  <section class="card card--front" aria-label="Card front">
    <header class="brand">
      <div class="brand__mark" aria-hidden="true"></div>
      <h2 class="brand__name">OAKLINE FURNISHINGS</h2>
      <p class="brand__tagline">TRADE FURNITURE SOLUTIONS</p>
    </header>

    <div class="details">
      <p class="person__name">MARCUS <span class="person__surname">DELANE</span></p>
      <p class="person__role">Managing Director</p>

      <address class="address">
        Trade Showroom &amp; Office<br>
        27B Harrow Trade Estate<br>
        Northfield London, N14 3QP
      </address>

      <ul class="contacts">
        <li><span class="contacts__label">T :</span>020 7946 0321</li>
        <li><span class="contacts__label">F :</span>020 7946 0388</li>
        <li><span class="contacts__label">M:</span>07700 90 04 17</li>
        <li><span class="contacts__label">E :</span>marcus@oakline.co.uk</li>
      </ul>
    </div>

    <div class="footer-rule"></div>
    <div class="footer-band">www.oakline.co.uk</div>
  </section>
</main>
</body>
</html>
```